Indonesian B2B Company (Varo Ingredients) - Stationery Design

Varo Ingredients needs a corporate, bold and professional-looking stationery design.

Varo Ingredients is a new Indonesian company manufacturing, marketing and distributing various ingredients / raw materials such as flavours, fragrance, colours, sweeteners, preservatives for the food & beverage, pharmaceutical, personal care and other household goods industries.

It is a business to business (B2B) company as we supply various natural and synthetic raw materials to various consumer goods manufacturers. We therefore need a logo/identity with corporate and industrial style.

Varo Ingredients is a startup company which belongs to a larger Tumina Jaya group of companies (http://tuminajaya.bizplank.example/about) that focuses in the mining, petroleum and energy businesses. Varo Ingredients would like to focus in providing good quality, safe, reliable and affordable ingredients for the industries. Our tagline is "Trusted Inputs, Lasting Growth"
Updates

We have updated some information including our requirements and contact details to be shown in the stationery. Please check the project brief.

Regards,

Varo Ingredients

Target Market(s)

Manufacturers of food & beverages, personal care, pharmaceutical and other FMCG factories.

Industry/Entity Type

Business

Requirements
Must have
• Smart, professional and corporate touches in the stationery designs. We require designs for:
1. Letterhead
2. Envelope (with and without window)
3. Name card
4. Powerpoint presentation template
5. CD label
6. Small memo / with compliments card

Contact details:

Company name:
PT Varo Ingredients

Address:
Ruko Pelita Sumber Asri, Blok K07 no: 15-16
Cempaka Hijau Utara, 14590
Indonesia

Tel:+62 21 738 2096
Fax:+62 21 738 2097
Email: info@varo-ingredients.example
Website: www.varo-ingredients.example

```html
<!DOCTYPE html>
<html lang="en">
<head>
<meta charset="utf-8">
<title>Varo Ingredients – Stationery</title>
<link href="https://fonts.googleapis.com/css2?family=Barlow:wght@400;600;700&display=swap" rel="stylesheet">
<style>
  :root{
    --red:#d5171f;
    --red-deep:#a40e16;
    --gold:#f4a41c;
    --ink:#3a3a3a;
    --paper:#ffffff;
    --backdrop:#e9e7e3;
  }
  *{box-sizing:border-box;margin:0;padding:0}
  html,body{width:1200px;height:900px;overflow:hidden}
  body{background:var(--backdrop);font-family:"Barlow",sans-serif;color:var(--ink);position:relative}
  address{font-style:normal}
  .sheet{position:absolute;background:var(--paper);box-shadow:0 3px 10px rgba(0,0,0,.18);overflow:hidden}
  .wave{position:absolute;left:0;bottom:0;width:100%}
  .brand{display:flex;align-items:center;gap:6px}
  .brand-mark{background:var(--red);flex:none}
  .brand-name{color:var(--red);font-weight:700;white-space:nowrap}
  .tagline{color:var(--ink);font-weight:400;white-space:nowrap}
  .site{position:absolute;color:#fff;font-weight:600;letter-spacing:.18em;white-space:nowrap}

  /* Letterhead */
  .letterhead{left:50px;top:105px;width:496px;height:705px}
  .letterhead .brand{position:absolute;left:34px;top:54px}
  .letterhead .brand-mark{width:14px;height:14px}
  .letterhead .brand-name{font-size:17px}
  .letterhead .tagline{position:absolute;left:34px;top:77px;font-size:8px}
  .letterhead .contact{position:absolute;right:24px;top:16px;width:152px;padding-left:10px;border-left:1px solid #d8d8d8;height:112px;text-align:right;font-size:7.5px;line-height:1.45}
  .contact .company{color:var(--red);font-weight:700;font-size:9.5px;margin-bottom:10px}
  .contact .gap{height:9px}
  .letterhead .site{left:12px;bottom:8px;font-size:8.5px}

  /* Business cards */
  .card{width:223px;height:120px;top:123px}
  .card-front{left:652px}
  .card-front .brand{position:absolute;left:12px;top:12px}
  .card-front .brand-mark{width:8px;height:8px}
  .card-front .brand-name{font-size:10px}
  .card-front .tagline{position:absolute;left:12px;top:27px;font-size:5px}
  .card-front .person{position:absolute;left:12px;top:58px;font-size:6px;line-height:1.4}
  .person .name{color:var(--red);font-weight:700;font-size:7px}
  .card-front .contact{position:absolute;left:108px;top:14px;width:84px;font-size:4.6px;line-height:1.45}
  .card-front .contact .company{font-size:5.5px;margin-bottom:4px}
  .card-front .contact .gap{height:4px}
  .card-back{left:885px;background:var(--red)}
  .card-back .brand{position:absolute;left:0;right:0;top:38px;justify-content:center}
  .card-back .brand-mark{width:10px;height:10px;background:#fff}
  .card-back .brand-name{color:#fff;font-size:14px}
  .card-back .site{left:0;right:0;bottom:9px;text-align:center;font-size:5.5px}

  /* Window envelope */
  .envelope-front{left:582px;top:275px;width:570px;height:245px}
  .envelope-front .brand{position:absolute;left:30px;top:30px}
  .envelope-front .brand-mark{width:12px;height:12px}
  .envelope-front .brand-name{font-size:15px}
  .envelope-front .tagline{position:absolute;left:30px;top:50px;font-size:7px}
  .envelope-front .window{position:absolute;left:30px;top:122px;width:200px;height:73px;border:1px solid #e5a0b4;border-radius:3px}
  .envelope-front .site{right:22px;bottom:7px;font-size:8.5px}

  /* Envelope back */
  .envelope-back{left:582px;top:540px;width:570px;height:245px}
  .envelope-back .flap{position:absolute;inset:0;width:100%;height:100%}
  .envelope-back .brand{position:absolute;left:0;right:0;top:28px;justify-content:center}
  .envelope-back .brand-mark{width:11px;height:11px}
  .envelope-back .brand-name{font-size:14px}
  .envelope-back .return{position:absolute;left:0;right:0;top:198px;text-align:center;font-size:7px;line-height:1.4}
  .return .company{color:var(--red);font-weight:700;font-size:9px}
  .return .rule{width:180px;height:1px;margin:0 auto 4px;background:linear-gradient(90deg,transparent,var(--gold),transparent)}
</style>
</head>
<body>

  <!-- Letterhead -->
  <section class="sheet letterhead">
    <div class="brand"><span class="brand-mark"></span><span class="brand-name">Varo Ingredients</span></div>
    <p class="tagline">Trusted Inputs, Lasting Growth</p>
    <address class="contact">
      <p class="company">PT Varo Ingredients</p>
      <p>Ruko Pelita Sumber Asri,</p>
      <p>Blok K07 no: 15-16</p>
      <p>Cempaka Hijau Utara, 14590</p>
      <p>Indonesia</p>
      <div class="gap"></div>
      <p>Tel:+62 21 738 2096</p>
      <p>Fax:+62 21 738 2097</p>
      <p>Email: info@varo-ingredients.example</p>
    </address>
    <svg class="wave" viewBox="0 0 496 70" preserveAspectRatio="none" height="70" aria-hidden="true">
      <path d="M0 40 C150 36 330 22 496 4 L496 70 L0 70Z" fill="var(--gold)"/>
      <path d="M0 44 C150 40 330 27 496 10 L496 70 L0 70Z" fill="var(--red)"/>
      <path d="M0 58 C160 56 330 48 496 30 L496 70 L0 70Z" fill="var(--red-deep)" opacity=".5"/>
    </svg>
    <p class="site">www.varo-ingredients.example</p>
  </section>

  <!-- Business card front -->
  <section class="sheet card card-front">
    <div class="brand"><span class="brand-mark"></span><span class="brand-name">Varo Ingredients</span></div>
    <p class="tagline">Trusted Inputs, Lasting Growth</p>
    <div class="person">
      <p class="name">Dimas Pratama</p>
      <p>Managing Director</p>
    </div>
    <address class="contact">
      <p class="company">PT Varo Ingredients</p>
      <p>Ruko Pelita Sumber Asri,</p>
      <p>Blok K07 no: 15-16</p>
      <p>Cempaka Hijau Utara, 14590</p>
      <p>Indonesia</p>
      <div class="gap"></div>
      <p>Tel: +62 21 738 2096</p>
      <p>Fax: +62 21 738 2097</p>
      <p>info@varo-ingredients.example</p>
    </address>
    <svg style="position:absolute;right:0;top:0;height:100%" width="30" viewBox="0 0 30 120" preserveAspectRatio="none" aria-hidden="true">
      <path d="M12 0 C2 40 2 80 10 120 L30 120 L30 0Z" fill="var(--gold)"/>
      <path d="M16 0 C6 40 6 80 14 120 L30 120 L30 0Z" fill="var(--red)"/>
    </svg>
  </section>

  <!-- Business card back -->
  <section class="sheet card card-back">
    <svg class="wave" viewBox="0 0 223 50" preserveAspectRatio="none" height="50" aria-hidden="true">
      <path d="M0 20 C70 40 150 30 223 8 L223 50 L0 50Z" fill="var(--red-deep)" opacity=".55"/>
    </svg>
    <div class="brand"><span class="brand-mark"></span><span class="brand-name">Varo Ingredients</span></div>
    <p class="site">www.varo-ingredients.example</p>
  </section>

  <!-- Window envelope -->
  <section class="sheet envelope-front">
    <div class="brand"><span class="brand-mark"></span><span class="brand-name">Varo Ingredients</span></div>
    <p class="tagline">Trusted Inputs, Lasting Growth</p>
    <div class="window" aria-hidden="true"></div>
    <svg class="wave" viewBox="0 0 570 60" preserveAspectRatio="none" height="60" aria-hidden="true">
      <path d="M0 36 C180 34 380 22 570 2 L570 60 L0 60Z" fill="var(--gold)"/>
      <path d="M0 40 C180 38 380 27 570 8 L570 60 L0 60Z" fill="var(--red)"/>
      <path d="M0 52 C200 50 380 42 570 26 L570 60 L0 60Z" fill="var(--red-deep)" opacity=".5"/>
    </svg>
    <p class="site">www.varo-ingredients.example</p>
  </section>

  <!-- Envelope back -->
  <section class="sheet envelope-back">
    <svg class="flap" viewBox="0 0 570 245" preserveAspectRatio="none" aria-hidden="true">
      <path d="M0 4 L230 95 Q285 110 340 95 L570 4" fill="none" stroke="#cfcfcf" stroke-width="1"/>
      <path d="M0 245 L130 90 M570 245 L440 90" fill="none" stroke="#dcdcdc" stroke-width="1"/>
    </svg>
    <div class="brand"><span class="brand-mark"></span><span class="brand-name">Varo Ingredients</span></div>
    <div class="return">
      <div class="rule"></div>
      <p class="company">PT Varo Ingredients</p>
      <p>Ruko Pelita Sumber Asri, Blok K07 no: 15-16 Cempaka Hijau Utara, 14590 Indonesia</p>
      <p>Tel: +62 21 738 2096 &nbsp; Fax: +62 21 738 2097 &nbsp; Email: info@varo-ingredients.example</p>
    </div>
  </section>

</body>
</html>
```